I need a better looking dashboard for my web application

I have a very table heavy web page that I would like to add a design touch to it. I have the logo and primary colors picked out, I just need some help in adding visual appeal the page. I would also like to add a couple of button to the page as shortcuts. Every spot that has a + sign could have a button added. I would also like to add another graph (the data will be in the uploaded files. Please feel free to ask any questions :-)

```html
<!DOCTYPE html>
<html lang="en">
<head>
<meta charset="utf-8">
<title>ShiftCover Dashboard</title>
<link href="https://fonts.googleapis.com/css2?family=Poppins:wght@400;500;600;700&display=swap" rel="stylesheet">
<style>
:root{
  --bg-dark:#1e1c32;
  --side-top:#4a3a78;
  --side-bot:#2b2245;
  --accent:#5e45a8;
  --accent-soft:#6b56b4;
  --ink:#1d1b2a;
  --muted:#8b8a99;
  --line:#ececf2;
  --panel:#f1f1f6;
  --green:#1f9d4a;
  --green-bg:#e3f6e8;
  --red:#e04848;
  --red-bg:#fde4e4;
  --orange:#ef8a24;
  --orange-bg:#fdebd6;
  --blue:#4e73df;
  --teal:#2bb0d0;
  --salmon:#f2907f;
  --badge:#1aa3e8;
}
*{box-sizing:border-box;margin:0;padding:0}
html,body{width:1200px;height:870px;overflow:hidden}
body{font-family:'Poppins',sans-serif;background:var(--bg-dark);color:var(--ink)}
.stage{position:absolute;left:0;top:0;width:1890px;height:1370px;transform:scale(.6349);transform-origin:0 0;
  background:radial-gradient(ellipse at 50% 10%,#2d2948 0%,var(--bg-dark) 60%)}
.abs{position:absolute}
.brand-top{left:0;width:1890px;top:110px;text-align:center;font-size:48px;font-weight:600;color:#6e58c8;letter-spacing:.5px}
.brand-top .dot{display:inline-block;width:22px;height:22px;border-radius:50%;background:var(--teal);margin-right:14px;vertical-align:middle;position:relative;top:-5px}
.app{left:225px;top:262px;width:1440px;height:932px;border-radius:22px;overflow:hidden;background:var(--panel)}
.side{left:0;top:0;width:240px;height:932px;background:linear-gradient(180deg,var(--side-top),var(--side-bot))}
.side-brand{left:0;width:240px;top:30px;text-align:center;color:#fff;font-size:22px;font-weight:600}
.side-brand .dot{display:inline-block;width:12px;height:12px;border-radius:50%;background:#fff;margin-right:8px}
.create{left:24px;top:112px;width:192px;height:50px;border-radius:25px;background:#fff;color:var(--accent);font-weight:600;font-size:14px;display:flex;align-items:center;padding-left:24px;gap:12px}
.create .ic{width:18px;height:20px;border-radius:3px;background:var(--accent);color:#fff;font-size:12px;display:flex;align-items:center;justify-content:center}
.nav{left:24px;width:192px;height:48px;border-radius:8px;display:flex;align-items:center;padding-left:16px;gap:16px;color:#fff;font-size:12.5px;font-weight:500}
.nav.active{background:var(--accent-soft)}
.nav .chev{margin-left:auto;margin-right:14px;font-size:11px}
.nav .count{margin-left:auto;margin-right:10px;width:18px;height:18px;border-radius:50%;background:var(--badge);font-size:9px;display:flex;align-items:center;justify-content:center}
.logout{left:24px;top:806px;width:192px;height:48px;border-radius:8px;background:#2a213f;color:var(--salmon);font-size:13px;display:flex;align-items:center;padding-left:16px;gap:14px}
.copy{left:24px;top:876px;width:200px;color:#cfc9e2;font-size:10.5px;line-height:15px}
.topbar{left:240px;top:0;width:1200px;height:72px;background:#fff;border-bottom:1px solid var(--line)}
.page-title{left:40px;top:18px;font-size:24px;font-weight:700}
.tabs{left:484px;top:18px;width:232px;height:36px;border-radius:6px;background:#e6e6ec;padding:2px;display:flex}
.tabs span{flex:1;display:flex;align-items:center;justify-content:center;font-size:12.5px;font-weight:500;color:var(--muted)}
.tabs .on{background:#fff;border-radius:5px;color:var(--accent);font-weight:600;border:1px solid #d6d3e6}
.bell{left:964px;top:26px}
.bell .n{position:absolute;left:12px;top:-8px;width:16px;height:16px;border-radius:50%;background:var(--badge);color:#fff;font-size:9px;display:flex;align-items:center;justify-content:center}
.user-av{left:1022px;top:19px;width:32px;height:32px;border-radius:50%;background:linear-gradient(135deg,#8aa0c9,#4b5c86)}
.user{left:1062px;top:20px;font-size:12.5px;font-weight:600;line-height:15px}
.user small{display:block;font-size:10.5px;font-weight:400;color:var(--muted)}
.caret{left:1140px;top:30px;color:#9a99a8;font-size:10px}
.h2{font-size:18px;font-weight:500}
.updated{left:860px;top:106px;font-size:10px;color:var(--muted)}
.card{background:#fff;border-radius:10px;box-shadow:0 1px 3px rgba(30,20,60,.06)}
.stats{left:280px;top:129px;width:792px;height:120px;display:flex}
.stat{flex:1;position:relative;padding:22px 0 0 24px}
.stat+.stat:before{content:"";position:absolute;left:0;top:24px;height:72px;border-left:1px solid var(--line)}
.stat b{display:block;font-size:20px;font-weight:600;line-height:24px}
.stat .lbl{font-size:11.5px;color:var(--muted);margin-top:4px}
.stat .d{margin-top:14px;font-size:11px;font-weight:500;display:flex;align-items:center;gap:7px}
.stat .d i{width:15px;height:15px;border-radius:50%;color:#fff;font-style:normal;font-size:9px;display:flex;align-items:center;justify-content:center}
.up{color:var(--green)} .up i{background:var(--green)}
.dn{color:var(--red)} .dn i{background:var(--red)}
.stat .ico{position:absolute;left:125px;top:32px;width:24px;height:24px;border-radius:6px}
.sect{left:280px;width:792px;overflow:hidden}
.sect-head{height:56px;display:flex;align-items:center;padding:0 16px;gap:10px}
.sect-head .t{font-size:15px;font-weight:600}
.search{margin-left:auto;width:220px;height:32px;border:1px solid #dedde6;border-radius:5px;font-size:10px;color:var(--muted);display:flex;align-items:center;padding:0 10px;justify-content:space-between}
.add{color:var(--accent);font-weight:600;font-size:13px;margin-left:22px;margin-right:12px;display:flex;align-items:center;gap:8px}
.grid{display:grid;align-items:center;padding-left:16px}
.thead{background:#f4f4f7;height:36px;font-size:8.5px;font-weight:600;color:#444;letter-spacing:.2px}
.thead span small{display:block;font-weight:400;color:var(--muted)}
.row{height:44px;border-bottom:1px solid var(--line);font-size:10.5px;position:relative}
.row.hl{background:#f7f6fa}
.g1{grid-template-columns:166px 106px 96px 156px 80px 1fr}
.g2{grid-template-columns:186px 126px 186px 106px 1fr}
.who{display:flex;align-items:center;gap:12px;font-weight:600}
.g2 .who{font-weight:400}
.av{width:24px;height:24px;border-radius:50%;flex:none}
.av.gen{background:#e4e4ec}
.pill{font-size:8px;font-weight:600;width:72px;height:20px;border-radius:4px;display:flex;align-items:center;justify-content:center}
.assigned{background:#eeeef1;color:#333}
.available{background:var(--green-bg);color:var(--green)}
.pending{background:var(--orange-bg);color:var(--orange)}
.approved{background:var(--green-bg);color:var(--green)}
.cancelled{background:var(--red-bg);color:var(--red)}
.ts{display:flex;gap:20px}
.ts em{font-style:normal;display:flex;align-items:center;gap:5px}
.ts em:before{content:"";width:9px;height:9px;border:1.3px solid #555;border-radius:50%}
.acts{position:absolute;right:16px;top:6px;display:flex;gap:12px}
.acts span{width:32px;height:32px;border-radius:50%;display:flex;align-items:center;justify-content:center}
.acts .w{background:#fff;box-shadow:0 1px 4px rgba(0,0,0,.12)}
.acts .p{background:var(--accent)}
.scroll{position:absolute;right:4px;width:4px;height:70px;border-radius:2px;background:#c9c8d2}
.fill{left:1104px;top:129px;width:296px;height:350px}
.fill .t,.pend .t{position:absolute;left:48px;top:18px;font-size:15px;font-weight:600}
.legend{position:absolute;left:16px;width:264px;font-size:10.5px}
.legend .bar{position:absolute;left:0;top:18px;width:130px;height:3px;background:#ececf2;border-radius:2px}
.legend .bar i{display:block;height:3px;border-radius:2px}
.legend .j{position:absolute;left:154px;top:12px}
.legend .j b{font-weight:600;margin-right:4px}
.legend .j span{color:var(--muted)}
.legend .pc{position:absolute;right:12px;top:12px;font-weight:600}
.pend{left:1104px;top:500px;width:296px;height:460px;background:#e8e7ef;border-radius:10px}
.pc-card{position:absolute;left:16px;width:264px;height:78px;background:#fff;border-radius:6px}
.pc-card .av{position:absolute;left:12px;top:15px;width:48px;height:48px}
.pc-card .nm{position:absolute;left:72px;top:10px;font-size:11px;font-weight:600}
.pc-card .st{position:absolute;left:72px;top:26px;font-size:10px;color:var(--muted);display:flex;gap:4px;align-items:center}
.pc-card .st i{width:11px;height:11px;border-radius:50%;background:var(--blue)}
.btns{position:absolute;left:72px;top:44px;display:flex;gap:8px}
.btns span{width:86px;height:23px;border-radius:4px;font-size:9px;font-weight:500;display:flex;align-items:center;justify-content:center;gap:5px}
.ok{border:1px solid var(--accent);color:var(--accent)}
.ok:before{content:"";width:9px;height:9px;border-radius:50%;background:var(--accent)}
.no{border:1px solid var(--red);color:var(--red)}
.no:before{content:"";width:7px;height:7px;border-radius:50%;border:1.2px solid var(--red)}
</style>
</head>
<body>
<div class="stage">
  <div class="abs brand-top"><span class="dot"></span>ShiftCover</div>

  <div class="abs app">
    <aside class="abs side">
      <div class="abs side-brand"><span class="dot"></span>ShiftCover</div>
      <div class="abs create"><span class="ic">+</span>Create absence</div>

      <div class="abs nav active" style="top:202px">
        <svg width="18" height="18" viewBox="0 0 18 18" fill="#fff"><rect x="1" y="1" width="16" height="6" rx="1.5"/><rect x="1" y="9" width="7" height="8" rx="1.5"/><rect x="10" y="9" width="7" height="8" rx="1.5"/></svg>Dashboard</div>
      <div class="abs nav" style="top:252px">
        <svg width="18" height="18" viewBox="0 0 18 18"><circle cx="9" cy="9" r="8" fill="#fff"/><circle cx="6" cy="8" r="2" fill="#3d3063"/><circle cx="12" cy="8" r="2" fill="#3d3063"/></svg>Regular Staff<span class="chev">&#8963;</span></div>
      <div class="abs nav" style="top:302px">
        <svg width="18" height="18" viewBox="0 0 18 18"><ellipse cx="9" cy="8" rx="8" ry="7" fill="#fff"/><path d="M4 13l-1 4 5-3z" fill="#fff"/><circle cx="6" cy="8" r="1" fill="#3d3063"/><circle cx="9" cy="8" r="1" fill="#3d3063"/><circle cx="12" cy="8" r="1" fill="#3d3063"/></svg>Messages<span class="count">8</span></div>
      <div class="abs nav" style="top:352px">
        <svg width="20" height="18" viewBox="0 0 20 18" fill="none" stroke="#fff" stroke-width="1.6"><rect x="1" y="2" width="18" height="12" rx="1.5"/><path d="M8 5.5l5 2.5-5 2.5z" fill="#fff"/><path d="M6 17h8"/></svg>Demo Outbox</div>
      <div class="abs nav" style="top:402px">
        <svg width="18" height="20" viewBox="0 0 18 20" fill="none" stroke="#fff" stroke-width="1.6"><circle cx="9" cy="7" r="5"/><path d="M5 11l-3 7 4-1 2 3M13 11l3 7-4-1-2 3"/></svg>Admin Location<span class="chev">&#8250;</span></div>
      <div class="abs nav" style="top:452px">
        <svg width="20" height="20" viewBox="0 0 20 20" fill="none" stroke="#fff" stroke-width="2"><circle cx="10" cy="10" r="3"/><circle cx="10" cy="10" r="7" stroke-dasharray="3 2.5"/></svg>Regular Services</div>

      <div class="abs logout"><svg width="18" height="16" viewBox="0 0 18 16" fill="none" stroke="#f2907f" stroke-width="1.8"><path d="M1 8h10M7 4l4 4-4 4M12 1h4v14h-4"/></svg>Log out</div>
      <div class="abs copy">Copyright © 2025. North Ridge Systems. All Rights Reserved. (v0.8.4)</div>
    </aside>

    <header class="abs topbar">
      <div class="abs page-title">Dashboard</div>
      <div class="abs tabs"><span class="on">Overview</span><span>Calendar</span></div>
      <div class="abs bell"><svg width="20" height="20" viewBox="0 0 20 20" fill="#8a8996"><path d="M10 2a5 5 0 0 0-5 5v5l-2 3h14l-2-3V7a5 5 0 0 0-5-5zM8 17a2 2 0 0 0 4 0z"/></svg><span class="n">4</span></div>
      <div class="abs user-av" role="img" aria-label="Profile photo of the signed-in manager"></div>
      <div class="abs user">Daniel R.<small>Manager</small></div>
      <div class="abs caret">&#9660;</div>
    </header>

    <div class="abs h2" style="left:280px;top:96px">Today’s summary</div>
    <div class="abs updated">&#8635;&nbsp; Last updated: 2 Jan 2025 at 10:48 AM</div>

    <div class="abs card stats">
      <div class="stat"><b>4</b><div class="lbl">Unfilled</div><div class="d up"><i>&#8593;</i>1.87%</div><span class="ico" style="background:#b35ad8"></span></div>
      <div class="stat"><b>13</b><div class="lbl">Filled</div><div class="d dn"><i>&#8595;</i>1.90%</div><span class="ico" style="background:var(--teal)"></span></div>
      <div class="stat"><b>29</b><div class="lbl">No sub needed</div><div class="d up"><i>&#8593;</i>2.06%</div><span class="ico" style="background:var(--blue)"></span></div>
      <div class="stat"><b>46</b><div class="lbl">Total</div><div class="d up"><i>&#8593;</i>1.02%</div><span class="ico" style="background:var(--accent)"></span></div>
    </div>

    <section class="abs card sect" style="top:268px;height:337px">
      <div class="sect-head">
        <svg width="20" height="16" viewBox="0 0 20 16" fill="#9a98b0"><circle cx="6" cy="5" r="3"/><circle cx="14" cy="5" r="3"/><path d="M0 15c0-4 3-6 6-6s6 2 6 6zM10 15c0-3 2-5 4-5s6 1 6 5z"/></svg>
        <span class="t">Manage openings</span>
        <span class="search">Seach staff, category<svg width="12" height="12" viewBox="0 0 12 12" fill="none" stroke="#5e45a8" stroke-width="1.8"><circle cx="5" cy="5" r="3.8"/><path d="M8 8l3 3"/></svg></span>
        <span class="add"><svg width="16" height="14" viewBox="0 0 16 14" fill="#5e45a8"><circle cx="10" cy="4" r="3"/><path d="M4 14c0-4 3-6 6-6s6 2 6 6z"/><rect x="0" y="6" width="6" height="1.8"/><rect x="2.1" y="3.9" width="1.8" height="6"/></svg>Add</span>
      </div>
      <div class="grid g1 thead"><span>REGULAR STAFF &#8595;</span><span>CATEGORY</span><span>STATUS &#8595;</span><span>SUMMARY</span><span>LOCATION</span><span>TIME SLOTS SUMMARY &#8595;</span></div>
      <div class="grid g1 row"><span class="who"><i class="av gen" role="img" aria-label="Empty staff placeholder"></i>Extra duty</span><span>Food service</span><span class="pill assigned">ASSIGNED</span><span>Immediate Need! This is a...</span><span>LJE</span><span class="ts">12/30 - 01/01<em>2h 30m</em></span></div>
      <div class="grid g1 row"><span class="who"><i class="av" style="background:#d9b07a" role="img" aria-label="Staff photo"></i>Mara Quill</span><span>Teacher</span><span class="pill available">AVAILABLE</span><span>Immediate Need! Mathem...</span><span>WDMS</span><span class="ts">02/12 - 02/16<em>4h 30m</em></span></div>
      <div class="grid g1 row hl"><span class="who"><i class="av" style="background:#6b6f7a" role="img" aria-label="Staff photo"></i>Tomas Vell</span><span>Bus Driver</span><span class="pill available">AVAILABLE</span><span>Urgent Hiring! We are in ne...</span><span>WDMS</span><span class="ts">02/03 - 02/07</span>
        <div class="acts"><span class="w"><svg width="10" height="12" viewBox="0 0 10 12" fill="#e04848"><rect x="0" y="1" width="10" height="2"/><rect x="1.5" y="3.5" width="7" height="8" rx="1"/></svg></span><span class="p"><svg width="12" height="12" viewBox="0 0 12 12" fill="#fff"><path d="M1 11l1-3 6-6 2 2-6 6z"/></svg></span></div></div>
      <div class="grid g1 row"><span class="who"><i class="av gen" role="img" aria-label="Empty staff placeholder"></i>Extra duty</span><span>Custodian</span><span class="pill assigned">ASSIGNED</span><span>Seeking sub for /couns...</span><span>FMS</span><span class="ts">01/06 - 01/10<em>3h 50m</em></span></div>
      <div class="grid g1 row"><span class="who"><i class="av" style="background:#3a2e2a" role="img" aria-label="Staff photo"></i>Owen Brantley</span><span>Teacher's Aide</span><span class="pill available">AVAILABLE</span><span>Urgent Hiring! We are in ne...</span><span>WDMS</span><span class="ts">02/03 - 02/07<em>3h 45m</em></span></div>
      <div class="grid g1 row"><span class="who"><i class="av gen" role="img" aria-label="Empty staff placeholder"></i>Extra duty</span><span>Custodian</span><span class="pill available">AVAILABLE</span><span>Seeking sub for /couns...</span><span>FMS</span><span class="ts">01/06 - 01/10<em>3h 50m</em></span></div>
      <span class="scroll" style="top:100px"></span>
    </section>

    <section class="abs card sect" style="top:625px;height:330px">
      <div class="sect-head">
        <svg width="14" height="18" viewBox="0 0 14 18" fill="#9a98b0"><path d="M1 1h8l4 4v12H1z"/></svg>
        <span class="t">Regular Staffs Leave Requests</span>
        <span class="search">Search name, assignment<svg width="12" height="12" viewBox="0 0 12 12" fill="none" stroke="#5e45a8" stroke-width="1.8"><circle cx="5" cy="5" r="3.8"/><path d="M8 8l3 3"/></svg></span>
      </div>
      <div class="grid g2 thead" style="height:44px"><span>FULL NAME &#8595;</span><span>ASSIGNMENT<small>(OPENING)</small></span><span>PRE-ARRANGED SUB<small>(OPENING)</small></span><span>STATUS &#8595;</span><span>TIME SLOTS SUMMARY &#8595;</span></div>
      <div class="grid g2 row"><span class="who"><i class="av" style="background:#e0b98e" role="img" aria-label="Staff photo"></i>June Halpern</span><span>Custodian</span><span class="who"><i class="av" style="background:#b07a52" role="img" aria-label="Substitute photo"></i>Rosa Kettel</span><span class="pill pending">PENDING</span><span class="ts">01/06 - 01/10<em>3h 50m</em></span></div>
      <div class="grid g2 row hl"><span class="who"><i class="av" style="background:#6b6f7a" role="img" aria-label="Staff photo"></i>Tomas Vell</span><span>Bus Driver</span><span class="who"><i class="av" style="background:#8a6a55" role="img" aria-label="Substitute photo"></i>Felix Dorne</span><span class="pill pending">PENDING</span><span class="ts">02/03 - 02/07</span>
        <div class="acts"><span class="w"><svg width="14" height="10" viewBox="0 0 14 10"><path d="M0 5q7-9 14 0-7 9-14 0z" fill="#5e45a8"/><circle cx="7" cy="5" r="2" fill="#fff"/></svg></span><span class="p"><svg width="12" height="12" viewBox="0 0 12 12" fill="#fff"><path d="M1 11l1-3 6-6 2 2-6 6z"/></svg></span></div></div>
      <div class="grid g2 row"><span class="who"><i class="av" style="background:#3a2e2a" role="img" aria-label="Staff photo"></i>Owen Brantley</span><span>Teacher's Aide</span><span class="who"><i class="av" style="background:#4a4040" role="img" aria-label="Substitute photo"></i>Andre Wolcott</span><span class="pill approved">APPROVED</span><span class="ts">02/03 - 02/07<em>3h 45m</em></span></div>
      <div class="grid g2 row"><span class="who"><i class="av" style="background:#555a62" role="img" aria-label="Staff photo"></i>Tess Marlow</span><span>Food service</span><span class="who"><i class="av" style="background:#9a5a50" role="img" aria-label="Substitute photo"></i>Clara Venn</span><span class="pill cancelled">CANCELLED</span><span class="ts">12/30 - 01/01<em>2h 30m</em></span></div>
      <div class="grid g2 row"><span class="who"><i class="av" style="background:#d9b07a" role="img" aria-label="Staff photo"></i>Mara Quill</span><span>Teacher</span><span class="who"><i class="av" style="background:#c9a070" role="img" aria-label="Substitute photo"></i>Ingrid Hale</span><span class="pill approved">APPROVED</span><span class="ts">02/12 - 02/16<em>4h 30m</em></span></div>
      <span class="scroll" style="top:110px"></span>
    </section>

    <section class="abs card fill">
      <svg class="abs" style="left:16px;top:18px" width="20" height="20" viewBox="0 0 20 20"><circle cx="10" cy="10" r="9" fill="#c9c7d6"/><path d="M10 1a9 9 0 0 1 0 18z" fill="#7f7d92"/></svg>
      <span class="t">Monthly fill rate</span>
      <svg class="abs" style="left:68px;top:54px" width="160" height="160" viewBox="0 0 160 160">
        <g transform="rotate(-90 80 80)" fill="none" stroke-width="18">
          <circle cx="80" cy="80" r="69" stroke="#5e45a8" stroke-dasharray="195.1 433.5"/>
          <circle cx="80" cy="80" r="69" stroke="#4e73df" stroke-dasharray="151.7 433.5" stroke-dashoffset="-195.1"/>
          <circle cx="80" cy="80" r="69" stroke="#2bb0d0" stroke-dasharray="86.7 433.5" stroke-dashoffset="-346.8"/>
        </g>
        <text x="80" y="82" text-anchor="middle" font-family="Poppins,sans-serif" font-size="24" font-weight="600" fill="#1d1b2a">45</text>
        <text x="80" y="101" text-anchor="middle" font-family="Poppins,sans-serif" font-size="11" fill="#8b8a99">Total Jobs</text>
      </svg>
      <div class="legend" style="top:228px">Open<span class="bar"><i style="width:60px;background:var(--accent)"></i></span><span class="j"><b>20</b><span>jobs</span></span><span class="pc">45%</span></div>
      <div class="legend" style="top:266px">Filled<span class="bar"><i style="width:40px;background:var(--blue)"></i></span><span class="j"><b>16</b><span>jobs</span></span><span class="pc">35%</span></div>
      <div class="legend" style="top:304px">No Sub<span class="bar"><i style="width:20px;background:var(--teal)"></i></span><span class="j"><b>9</b><span>jobs</span></span><span class="pc">20%</span></div>
    </section>

    <section class="abs pend">
      <svg class="abs" style="left:16px;top:18px" width="22" height="20" viewBox="0 0 22 20"><path d="M11 1l10 18H1z" fill="#8a889c"/><rect x="10" y="7" width="2" height="6" fill="#fff"/><rect x="10" y="15" width="2" height="2" fill="#fff"/></svg>
      <span class="t">Pending Profile Images</span>
      <div class="pc-card" style="top:56px"><i class="av" style="background:#6a4030" role="img" aria-label="Submitted profile image"></i><span class="nm">Lena Farrow</span><span class="st">None-verified</span><div class="btns"><span class="ok">Approve</span><span class="no">Decline</span></div></div>
      <div class="pc-card" style="top:139px"><i class="av" style="background:#8a6a5a" role="img" aria-label="Submitted profile image"></i><span class="nm">Ivo Marsh</span><span class="st"><i></i>Verified</span><div class="btns"><span class="ok">Approve</span><span class="no">Decline</span></div></div>
      <div class="pc-card" style="top:222px"><i class="av" style="background:#3a3636" role="img" aria-label="Submitted profile image"></i><span class="nm">Reid Callow</span><span class="st">None-verified</span><div class="btns"><span class="ok">Approve</span><span class="no">Decline</span></div></div>
      <div class="pc-card" style="top:305px"><i class="av" style="background:#c05a3a" role="img" aria-label="Submitted profile image"></i><span class="nm">Nina Corbet</span><span class="st">None-verified</span><div class="btns"><span class="ok">Approve</span><span class="no">Decline</span></div></div>
      <div class="pc-card" style="top:388px"><i class="av" style="background:#9a5a48" role="img" aria-label="Submitted profile image"></i><span class="nm">Colin Ashby</span><span class="st"><i></i>Verified</span></div>
    </section>
  </div>
</div>
</body>
</html>
```